Action Jacket 8.5 X 11 double pocket folder requiring action

This folder will be mailed to a prospect when telephonically requested by the prospect.

It will have our logo on the front cover with a "tagline" marketing the attendant service on the front page in the space below the logo.

Tag line: Tessaron Turns Panic Into a Plan for Homeowners

Saving Foreclosure victims with the Short-Sale one at time with proven results.

The back cover can be used.

Further points:

Tessaron primarily does Short-Sales
The Seller pays nothing.
THE SELLER PAYS NOTHING!!
Tessaron pays the attorneys that negotiate on behalf of the Seller.
Negotiations are always done by highly specialized attorneys/paralegals.
Tessaron is a word from Leviticus in the Old Testament. It means "Forgiveness of debt, return of property to its rightful owner and freeing of the slaves."

Seller expectations:
1. 3 to 6 extra months in your home; save rent.
2. Guaranteed "Waiver of Deficiency"
3. Almost all Tessaron Sellers will attain a minimum of $3,000 relocation allowance, many are now receiving $10,000.
4. FORECLOSUE eliminated from the Credit Report

Target Market(s)

The prospect has already responded to a mail piece and agreed telephonically to List their home. This piece is designed to re-enforce their decision and memorialize their decision on paper.
This piece will be a response mailer being sent OVERNIGHT with forms to sign and return in a provided postage-paid OVERNIGHT return envelope. These are people facing the ANXIETY of the unknown having their homes auctioned at the end of a multi-year ordeal of foreclosure. They have many unanswered questions many of which cannot be answered at this time. This piece must be designed to emphasise and overcome their natural tendancy to hesitate. They all face an AUCTION DATE and time is of the essence. We have lost many clients due to their inability to make a decision and/or ambivalence. They then lose their homes while staring into the headlights like a deer.

Font styles to use
Serif
Other font styles liked:
• See Tessaron Logo font

Requirements
Must have
• Short to the point message/s
• Crisp design
• Action demanding content
Should not have
• clutter

```html
<!DOCTYPE html>
<html lang="en">
<head>
<meta charset="utf-8">
<title>Tessaron Real Estate Corporation – Folder Cover</title>
<link rel="stylesheet" href="https://fonts.googleapis.com/css2?family=DM+Serif+Display&family=Tinos&display=swap">
<style>
  :root {
    --navy: #1d3a6c;
    --gold: #e8a900;
    --ink: #1a1a1a;
    --paper-light: #ffffff;
    --paper-edge: #e6e6e6;
    --skyline-dark: #1f2634;
    --skyline-mid: #3a4354;
    --skyline-haze: #b7bcc5;
    --pattern-tint: #e3e3e3;
  }
  * { margin: 0; padding: 0; box-sizing: border-box; }
  html, body { width: 849px; height: 1200px; overflow: hidden; background: var(--paper-edge); }
  .cover {
    position: relative;
    width: 849px;
    height: 1200px;
    overflow: hidden;
    background: radial-gradient(ellipse 70% 55% at 50% 43%, var(--paper-light) 0%, #f6f6f6 45%, var(--paper-edge) 100%);
    border: 1px solid #d6d6d6;
  }
  .brand {
    position: absolute;
    right: 140px;
    top: 190px;
    text-align: right;
  }
  .brand-name-row {
    display: flex;
    align-items: center;
    justify-content: flex-end;
    gap: 22px;
  }
  .brand-square {
    width: 46px;
    height: 46px;
    background: var(--gold);
  }
  .brand-name {
    font-family: "DM Serif Display", serif;
    font-size: 112px;
    line-height: 1;
    color: var(--navy);
    letter-spacing: -1px;
  }
  .brand-descriptor {
    font-family: "DM Serif Display", serif;
    font-size: 36px;
    line-height: 1;
    color: var(--navy);
    margin-top: 6px;
  }
  .tagline {
    font-family: "Tinos", serif;
    font-size: 19px;
    color: var(--ink);
    margin-top: 10px;
  }
  .pattern-area {
    position: absolute;
    left: 0;
    top: 700px;
    width: 640px;
    height: 380px;
    background: radial-gradient(ellipse at 50% 50%, var(--pattern-tint) 0%, rgba(227,227,227,0) 70%);
    opacity: 0.7;
  }
  .skyline {
    position: absolute;
    left: 0;
    bottom: 0;
    width: 849px;
    height: 200px;
    background: linear-gradient(180deg, var(--skyline-haze) 0%, var(--skyline-mid) 40%, var(--skyline-dark) 100%);
  }
</style>
</head>
<body>
  <main class="cover">
    <header class="brand">
      <div class="brand-name-row">
        <span class="brand-square" aria-hidden="true"></span>
        <h1 class="brand-name">Tessaron</h1>
      </div>
      <p class="brand-descriptor">Real Estate Corporation</p>
      <p class="tagline">Tessaron Turns Panic Into a Plan for Homeowners</p>
    </header>
    <div class="pattern-area" role="img" aria-label="Faint decorative background pattern"></div>
    <div class="skyline" role="img" aria-label="Illustrated city skyline of dark office towers along the bottom edge"></div>
  </main>
</body>
</html>
```